Make it cool to work near where you are...

Calling all creatives - create the ultimate cool card for people who want to cut their commute.

Here at TilloPod we've got what can best be described as an Marlin pass for desks - and we want to brighten up the wallets of our most loyal users.

So, pitch us your ideas and you might see your design on cards being flashed across the country - and we've thrown in a bit of cash too.

Do see our brief card guidelines - with a couple of past examples thrown in.

Industry/Entity Type

Cash

```html
<!DOCTYPE html>
<html lang="en">
<head>
<meta charset="utf-8">
<title>TilloPod Card</title>
<link rel="stylesheet" href="https://fonts.googleapis.com/css2?family=Open+Sans:wght@400;700&display=swap">
<style>
  :root {
    --ink: #3e3a3b;
    --paper: #ffffff;
    --roof-orange: #f0894a;
    --roof-pink: #e0197d;
    --roof-rose: #f2a6c8;
    --roof-purple: #7b4a9c;
    --roof-teal: #5fa8b4;
    --roof-yellow: #f2c23a;
    --roof-red: #c8283c;
    --roof-lime: #b6cc3a;
  }
  html, body {
    margin: 0;
    padding: 0;
    width: 1200px;
    height: 754px;
    overflow: hidden;
    background: var(--paper);
  }
  .card {
    position: relative;
    width: 1200px;
    height: 754px;
    overflow: hidden;
    background: var(--paper);
    font-family: "Open Sans", sans-serif;
  }
  .rooftops-pattern {
    position: absolute;
    left: 0;
    top: 0;
    width: 1200px;
    height: 610px;
    background:
      linear-gradient(180deg, rgba(255,255,255,0.18) 0%, rgba(255,255,255,0) 40%, rgba(62,58,59,0.35) 100%),
      linear-gradient(100deg,
        var(--roof-orange) 0%,
        var(--roof-rose) 12%,
        var(--roof-lime) 22%,
        var(--roof-purple) 34%,
        var(--roof-pink) 46%,
        var(--roof-red) 58%,
        var(--roof-teal) 68%,
        var(--roof-yellow) 80%,
        var(--roof-orange) 92%,
        var(--roof-red) 100%);
  }
  .footer-band {
    position: absolute;
    left: 0;
    top: 610px;
    width: 1200px;
    height: 144px;
    background: var(--ink);
  }
  .web-address {
    position: absolute;
    left: 0;
    width: 1200px;
    top: 658px;
    margin: 0;
    text-align: center;
    color: var(--paper);
    font-size: 44px;
    font-weight: 400;
    line-height: 1;
  }
  .brand-mark {
    position: absolute;
    left: 912px;
    top: 558px;
    width: 192px;
    height: 84px;
    box-sizing: border-box;
    display: flex;
    align-items: center;
    justify-content: center;
    gap: 10px;
    background: var(--ink);
    border: 4px solid var(--paper);
    border-radius: 12px;
  }
  .brand-mark .brand-square {
    width: 18px;
    height: 18px;
    background: var(--roof-pink);
  }
  .brand-mark .brand-name {
    color: var(--paper);
    font-size: 30px;
    font-weight: 700;
    line-height: 1;
  }
</style>
</head>
<body>
  <div class="card">
    <div class="rooftops-pattern" role="img" aria-label="Repeating pattern of dark grey houses and apartment blocks topped with colourful roof chevrons"></div>
    <div class="footer-band"></div>
    <div class="brand-mark">
      <span class="brand-square"></span>
      <span class="brand-name">TilloPod</span>
    </div>
    <p class="web-address">www.tillopod.com</p>
  </div>
</body>
</html>
```